Law Firm Logo and Stationary

I need a logo for my law firm.  The logo should only contain the firm name "Halvey & Halvey, P.C." but we are open to slight additions like underlining or a box.  We are looking for a modern style but not edgy because our target market is businesses and corporations.

I would like a logo that invokes the traditional values of a law firm (trust, integrity, knowledge) but I want an updated look.

To be clear, the logo should only contain the firm name, I am just looking for a font treatment.

The logo color is up to you.  The only initial opinion I have is that bright colors may not fit with the professional look of a law firm. 

I also want to incorporate the new logo into letterhead and business card designs.  The letterhead should include all of the information that is in my current letterhead, which is attached.  The letterhead should be black or grey on white.  The colored logo will go on the website and promotional materials.

For the business card, I would like to have the logo on the top left, the employee name (Colin T. Halvey) on the middle left and the firm information (address, tel, fax, website, email) on right side.  I am open to suggestions if you have better ideas.
Updates

Here are some comments on the initial 8 designs:

a) I am just interested in a font treatment of our firm name, "Halvey & Halvey, P.C."  I do not want any graphics like a gavel or shield. 

b) The full name of the firm must be in the logo.  So I cannot use designs that only have "H & H"

c) EXAMPLES: Here are two websites with examples of law firm logos that just have the firm name.  These are just samples to give you a general idea of what I am looking for.  Check out:  www.qz-legal.example and www.marrowfieldtate.example 

In short, I am looking for a simple, clean design that will look modern enough for our website but is also conservative enough to be on letterhead that gets sent to judges and other lawyers.

Also, the sample letterhead is now loaded in the brief so you can see the information I need included in the new letterhead.

Thanks.

Target Market(s)

businesses and corporations.

Industry/Entity Type

Law Firm

Logo Text

Halvey & Halvey, P.C.

Requirements
Must have
• Firm name, "Halvey & Halvey, P.C."

```html
<!DOCTYPE html>
<html lang="en">
<head>
<meta charset="utf-8">
<title>Halvey &amp; Halvey, P.C. — Identity</title>
<link rel="stylesheet" href="https://fonts.googleapis.com/css2?family=Michroma&display=swap">
<style>
  :root {
    --ink: #0c0d0e;
    --gold: #d9a000;
    --paper: #ffffff;
  }
  * { margin: 0; padding: 0; box-sizing: border-box; }
  html, body {
    width: 1200px; height: 929px; overflow: hidden;
    background: var(--paper);
  }
  body {
    position: relative;
    font-family: "Michroma", "Arial", sans-serif;
    color: var(--ink);
  }
  .wordmark {
    position: absolute;
    color: var(--ink);
    white-space: nowrap;
    letter-spacing: 0.01em;
    line-height: 1;
  }
  .wordmark--master { left: 150px; top: 50px; width: 920px; text-align: center; font-size: 46px; }
  .wordmark--letterhead { left: 10px; top: 238px; font-size: 24px; }
  .wordmark--card { left: 41px; top: 62px; font-size: 18.5px; }

  .letterhead__contact, .letterhead__partners {
    position: absolute;
    list-style: none;
    font-variant: small-caps;
    white-space: nowrap;
  }
  .letterhead__contact { left: 10px; top: 296px; font-size: 19px; line-height: 30px; letter-spacing: 0.16em; }
  .letterhead__contact .gap { margin-top: 20px; }
  .letterhead__partners { left: 753px; top: 256px; font-size: 17px; line-height: 29.5px; letter-spacing: 0.1em; }
  .letterhead__partners .gap { margin-top: 31px; }
  .letterhead__rule {
    position: absolute; left: 3px; right: 0; top: 508px; height: 6px;
    background: var(--ink);
  }

  .card {
    position: absolute; left: 293px; top: 578px; width: 614px; height: 351px;
    background: var(--gold);
    border-radius: 22px;
    overflow: hidden;
  }
  .card__name {
    position: absolute; left: 40px; top: 180px;
    font-size: 20px; font-variant: small-caps; letter-spacing: 0.14em;
    white-space: nowrap; line-height: 1;
  }
  .card__title {
    position: absolute; right: 336px; top: 205px;
    font-size: 10px; font-variant: small-caps; letter-spacing: 0.14em;
    white-space: nowrap;
  }
  .card__panel {
    position: absolute; left: 299px; right: 0; top: 164px; height: 92px;
    background: var(--ink); color: var(--paper);
    padding: 19px 0 0 14px;
    font-size: 9.4px; line-height: 14px; letter-spacing: 0.14em;
    font-variant: small-caps; white-space: nowrap;
  }
  .card__stripe { position: absolute; left: 299px; right: 0; background: var(--ink); }
  .card__stripe--one { top: 262px; height: 28px; }
  .card__stripe--two { top: 296px; height: 22px; }
</style>
</head>
<body>
  <div class="wordmark wordmark--master">HALVEY &amp; HALVEY, P.C.</div>

  <section class="letterhead">
    <div class="wordmark wordmark--letterhead">HALVEY &amp; HALVEY, P.C.</div>
    <ul class="letterhead__contact">
      <li>2750 Linden Avenue</li>
      <li>Fairmont, MD 20915</li>
      <li>Tel 301.555.0142&nbsp;&nbsp;Fax 301.555.0178</li>
      <li>www.halveypc.example</li>
      <li class="gap">Writer’s email</li>
      <li>walter.halvey@halveypc.example</li>
    </ul>
    <ul class="letterhead__partners">
      <li>WALTER E. HALVEY†#</li>
      <li>COLIN T. HALVEY†*</li>
      <li>MORRIS HALVEY (1916-1994)</li>
      <li class="gap">ADMITTED TO PRACTICE</li>
      <li>†District of Columbia</li>
      <li>#Maryland</li>
      <li>*New York</li>
    </ul>
    <div class="letterhead__rule"></div>
  </section>

  <section class="card">
    <div class="wordmark wordmark--card">HALVEY &amp; HALVEY, P.C.</div>
    <div class="card__name">Colin T. Halvey</div>
    <div class="card__title">Legal Consultant</div>
    <div class="card__panel">
      2750 Linden Avenue<br>
      Fairmont, MD 20915<br>
      Tel 301.555.0142&nbsp;&nbsp;Fax 301.555.0178<br>
      www.halveypc.example
    </div>
    <div class="card__stripe card__stripe--one"></div>
    <div class="card__stripe card__stripe--two"></div>
  </section>
</body>
</html>
```